Save our Business Card - We need your help

We need a fresh look on our business cards. We like it as it is, but it's not quite getting the 'wow' effect that we desire.
We're a tech startup building a cloud based solution for retailers consisting of Point of Sale, Inventory management and CRM.
The design should communicate a sense of a company that cares about the little things, design and relationships.
You can have a look at our website www.tillnest.com to get a feel for what we're like. Please feel free to message us for any further clarification
Target Market(s)
Our Customers are retail busines owners, cafe owners, other startups etc.
Industry/Entity Type
Building
Colors
Designer to choose colors to be used in the design.
Look and feel
Each slider illustrates characteristics of the customer's brand and the style your logo design should communicate.

```html
<!DOCTYPE html>
<html lang="en">
<head>
<meta charset="utf-8">
<title>TillNest Business Card</title>
<link rel="stylesheet" href="https://fonts.googleapis.com/css2?family=Questrial&display=swap">
<style>
  :root {
    --page: #ffffff;
    --label: #8a8a8a;
    --card-dark: #1e2021;
    --card-glow: #3a3c3d;
    --orange: #e08424;
    --orange-edge: #ef5a24;
    --text-light: #ffffff;
    --mark-faint: #56595b;
  }
  * { margin: 0; padding: 0; box-sizing: border-box; }
  html, body {
    width: 1200px; height: 431px; overflow: hidden;
    background: var(--page);
    font-family: "Questrial", sans-serif;
  }
  .sheet { position: relative; width: 1200px; height: 431px; }
  .side-label {
    position: absolute; top: 31px;
    font-size: 11px; color: var(--label); letter-spacing: 0.3px;
  }
  .side-label--front { left: 33px; }
  .side-label--back { left: 601px; }
  .card-art { position: absolute; left: 0; top: 0; }
  .brand {
    position: absolute; left: 123px; top: 212px;
    display: flex; align-items: center; gap: 9px;
  }
  .brand-square { width: 40px; height: 40px; background: var(--orange); }
  .brand-name {
    font-size: 29px; color: var(--text-light); letter-spacing: 0.2px;
  }
  .card-text { position: absolute; color: var(--text-light); white-space: nowrap; }
  .website { left: 458px; top: 339px; font-size: 13.5px; letter-spacing: 0.3px; }
  .holder-name { left: 614px; top: 64px; font-size: 25px; letter-spacing: 0.3px; }
  .holder-role { left: 614px; top: 92px; font-size: 11px; }
  .contact-list { left: 614px; top: 259px; font-size: 13px; line-height: 16px; list-style: none; }
  .contact-list li { display: flex; margin-bottom: 7px; }
  .contact-key { width: 14px; font-size: 10px; opacity: 0.85; }
  .contact-list .address { margin-bottom: 0; }
</style>
</head>
<body>
<main class="sheet">
  <span class="side-label side-label--front">Front</span>
  <span class="side-label side-label--back">Back</span>

  <svg class="card-art" width="1200" height="431" viewBox="0 0 1200 431" aria-hidden="true">
    <defs>
      <radialGradient id="frontGlow" cx="170" cy="235" r="260" gradientUnits="userSpaceOnUse">
        <stop offset="0" stop-color="var(--card-glow)"/>
        <stop offset="1" stop-color="var(--card-dark)"/>
      </radialGradient>
      <radialGradient id="backGlow" cx="1110" cy="230" r="200" gradientUnits="userSpaceOnUse">
        <stop offset="0" stop-color="var(--card-glow)"/>
        <stop offset="1" stop-color="var(--card-dark)"/>
      </radialGradient>
    </defs>
    <!-- front card -->
    <rect class="card-front" x="34" y="54" width="567" height="314" fill="url(#frontGlow)"/>
    <polygon points="601,54 463,54 335,238 410,368 601,368" fill="var(--orange-edge)"/>
    <polygon points="601,54 466,54 339,238 413,368 601,368" fill="var(--orange)"/>
    <!-- back card -->
    <rect class="card-back" x="603" y="54" width="568" height="314" fill="url(#backGlow)"/>
    <polygon points="603,54 910,54 1039,242 963,368 603,368" fill="var(--orange-edge)"/>
    <polygon points="603,54 907,54 1036,242 960,368 603,368" fill="var(--orange)"/>
    <rect class="back-mark" x="1108" y="304" width="40" height="40" fill="var(--mark-faint)"/>
  </svg>

  <div class="brand">
    <span class="brand-square"></span>
    <span class="brand-name">TillNest</span>
  </div>
  <p class="card-text website">www.tillnest.com</p>

  <h1 class="card-text holder-name">Mr. Alan Reyes</h1>
  <p class="card-text holder-role">CEO and Co Founder</p>
  <ul class="card-text contact-list">
    <li><span class="contact-key">T.</span><span>+(603) 2210 4470</span></li>
    <li><span class="contact-key">E.</span><span>support@tillnest.com</span></li>
    <li class="address"><span class="contact-key">A.</span><span>Unit B-3-12, Block A4 Parkview<br>Jalan Cahaya PJU3 47810<br>Kota Damansara Selangor, Malaysia</span></li>
  </ul>
</main>
</body>
</html>
```